| 希望する色 | 特になし・その他 追記事項: 周囲の景色に埋没しないような色合いを希望します。 |
戸建賃貸住宅6棟の計画「ソライロテラス・ミナモト」の看板デザインの依頼です。 【 概要 】 全6棟の戸建賃貸住宅を建築中です。 建築地が住宅街の中にあり場所がわかりにくいため、大通りから見える場所へ看板を掲出したいと考えています。 周辺にある戸建賃貸住宅は規格モノを建てただけですが、地元工務店と組んで自然環境を重視した計画としました。 賃貸住宅でも環境重視の方、都市部から郊外へ引っ越しをしてくる方、などにアピールしたいと思っています。 シンプルかつデザイン性の高い看板デザインを募集します。 【 依頼内容 】 ・看板サイズ:横3,000mm × 縦2,000mm ・看板の素材:メッシュターポリン(予定) ・デザイン素材:計画名のロゴは用意したものを使用してください。他はお任せします。 ・デザイン内容:「戸建賃貸住宅」は明示してください。建築地案内は矢印程度で良いかと考えています。敷地レイアウトの明示は不要です。 ・デザインの利用について:看板への使用が主目的ですが、HPへの掲載、不動産仲介業者への配布等も行う場合があります。作成デザインを尊重し編集、合成、切り抜き等は原則行いません。他制限事項あればお知らせください。 【 契約金額(税抜) 】 70,000円(税別) ※契約金額(税込)からシステム利用料を差し引いた金額が、ワーカーさまの受取金額となります その他ご質問等ありましたら、気軽にお問い合わせください。 ご応募をお待ちしております! |
| 参考記事URL | ||
| https://fuyukobo-homes.example.net | ||
採用の理由
シンプルでもバランスが良く看板の目的に合致したデザインでした。
応募者全員へのお礼・コメント
沢山のご提案ありがとうございました。良い案が幾つもあり採用デザインを1つに絞るのは悩みました。また機会がありましたらよろしくお願いします。

```html
<!DOCTYPE html>
<html lang="ja">
<head>
<meta charset="UTF-8">
<title>ソライロテラス・ミナモト 看板</title>
<link href="https://fonts.googleapis.com/css2?family=Noto+Serif+JP:wght@500;700;900&display=swap" rel="stylesheet">
<style>
  :root {
    --ink: #1a1a1a;
    --accent-red: #d9261c;
    --band-lime: #e4e94a;
    --paper: #ffffff;
    --leaf-dark: #4f7a2c;
    --leaf-mid: #7ea447;
    --leaf-light: #b9cf8c;
    --wall: #eef0ef;
  }
  html, body {
    margin: 0;
    padding: 0;
    width: 1200px;
    height: 1200px;
    overflow: hidden;
    background: var(--paper);
  }
  body {
    position: relative;
    font-family: "Noto Serif JP", serif;
    color: var(--ink);
  }
  .signboard {
    position: absolute;
    left: 75px;
    top: 227px;
    width: 1077px;
    height: 725px;
    overflow: hidden;
    background: var(--paper);
    box-shadow: 0 0 0 1px #dcdcdc;
  }
  .scene-photo {
    position: absolute;
    inset: 0 0 72px 0;
    background:
      radial-gradient(ellipse 34% 52% at 50% 55%, var(--leaf-dark) 0%, var(--leaf-mid) 45%, rgba(185,207,140,0.6) 75%, rgba(255,255,255,0) 100%),
      linear-gradient(90deg, #ffffff 0%, var(--wall) 30%, #e3e6e4 50%, var(--wall) 70%, #ffffff 100%);
  }
  .headline-type {
    position: absolute;
    left: 32px;
    top: 36px;
    margin: 0;
    font-size: 58px;
    font-weight: 900;
    letter-spacing: 0;
    text-shadow: 0 0 12px #fff, 0 0 6px #fff;
  }
  .count-stack {
    position: absolute;
    left: 32px;
    top: 150px;
    width: 420px;
    margin: 0;
    font-weight: 900;
    line-height: 1;
    text-shadow: 0 0 14px #fff, 0 0 6px #fff;
  }
  .count-stack .big-char {
    display: block;
    width: 290px;
    text-align: center;
    font-size: 132px;
    height: 132px;
  }
  .count-stack .big-char.number {
    color: var(--accent-red);
    font-size: 124px;
    height: 124px;
  }
  .count-stack .status {
    display: block;
    font-size: 104px;
    margin-top: 6px;
    letter-spacing: -2px;
  }
  .tagline {
    position: absolute;
    right: 50px;
    top: 26px;
    height: 620px;
    margin: 0;
    writing-mode: vertical-rl;
    font-size: 54px;
    font-weight: 900;
    line-height: 1.45;
    text-shadow: 0 0 12px #fff, 0 0 6px #fff;
  }
  .tagline .season { color: var(--accent-red); }
  .tagline .project-name { padding-top: 70px; }
  .info-band {
    position: absolute;
    left: 0;
    right: 0;
    bottom: 0;
    height: 72px;
    background: var(--band-lime);
    display: flex;
    align-items: center;
    padding: 0 20px;
    box-sizing: border-box;
    font-weight: 700;
  }
  .builder-name {
    display: flex;
    align-items: center;
    gap: 8px;
    font-size: 26px;
    font-weight: 700;
    width: 220px;
  }
  .builder-name .mark {
    width: 22px;
    height: 22px;
    background: var(--ink);
  }
  .project-title {
    font-size: 40px;
    font-weight: 500;
    margin-left: 10px;
    letter-spacing: 1px;
  }
  .opening-note {
    margin-left: auto;
    font-size: 40px;
    font-weight: 700;
    letter-spacing: 1px;
  }
  .opening-note .season { color: var(--accent-red); }
</style>
</head>
<body>
  <div class="signboard">
    <div class="scene-photo" role="img" aria-label="白い戸建住宅が並ぶ街並みの中央に大きく茂る緑の樹木の写真"></div>

    <p class="headline-type">「戸建賃貸住宅」</p>

    <h1 class="count-stack">
      <span class="big-char">全</span>
      <span class="big-char number">6</span>
      <span class="big-char">棟</span>
      <span class="status">建築中!</span>
    </h1>

    <p class="tagline"><span class="season">四季</span>が感じられる、<br><span class="project-name">ソライロテラス。</span></p>

    <div class="info-band">
      <div class="builder-name"><span class="mark"></span>ミナモトハウス</div>
      <div class="project-title">ソライロテラス・ミナモト</div>
      <div class="opening-note"><span class="season">来春</span>公開予定。</div>
    </div>
  </div>
</body>
</html>
```